Glidewell Depot logo

Glidewell Depot is owned and operated by industry professionals with years of direct experience in providing customers with the right equipment to suit their needs. Our specialty lies within dealing in the Halvern Medical range of products. Our product range is suited to both the new user and for those that know what they want, a full line of products ranging from ultra-light wheelchairs, wheelchairs for sport and recreation and paediatric or just everyday use.

Industry/Entity Type

Recreation

Contact Information for Business Card

name, title, landline,fax,mobile,email,web address,physical address,logo,possibly a wheelchair pic

Requirements
Must have
• logo - uploaded
Nice to have
• colour scheme consistent with
www.glidewelldepot.com.au

```html
<!DOCTYPE html>
<html lang="en">
<head>
<meta charset="utf-8">
<title>Glidewell Depot – Business Card</title>
<link rel="stylesheet" href="https://fonts.googleapis.com/css2?family=Arimo:wght@400;700&family=Roboto+Condensed:wght@700&display=swap">
<style>
  :root {
    --page-bg: #e8e6e3;
    --card-bg: #ffffff;
    --brand-purple: #6b2a5c;
    --brand-purple-dark: #5a2150;
    --brand-blue: #1f5c96;
    --ink-light: #f3eef2;
    --photo-light: #d9dadc;
    --photo-dark: #5d6064;
  }
  * { box-sizing: border-box; margin: 0; padding: 0; }
  html, body {
    width: 1200px; height: 900px; overflow: hidden;
    background: var(--page-bg);
    font-family: "Arimo", Arial, sans-serif;
  }
  .sheet {
    position: relative; width: 1200px; height: 900px;
  }
  .card {
    position: absolute; left: 285px;
    width: 630px; height: 350px;
    background: var(--card-bg);
    border-radius: 12px;
    overflow: hidden;
    box-shadow: 0 6px 18px rgba(0,0,0,.18);
  }
  .card--back { top: 70px; }
  .card--front { top: 480px; }

  .brand {
    position: absolute; left: 30px; top: 30px;
    display: flex; align-items: center; gap: 10px;
  }
  .brand__dot {
    width: 30px; height: 30px; border-radius: 50%;
    background: var(--brand-blue);
  }
  .brand__name {
    font-family: "Arimo", Arial, sans-serif;
    font-weight: 400; font-size: 30px;
    color: var(--brand-purple);
    white-space: nowrap;
  }
  .tagline {
    position: absolute; left: 30px; top: 86px;
    font-weight: 700; font-size: 13px; letter-spacing: .3px;
    color: var(--brand-blue);
    white-space: nowrap;
  }
  .product-photo {
    position: absolute;
    background: radial-gradient(ellipse at 55% 50%, var(--photo-light) 0%, #a9abae 55%, var(--photo-dark) 100%);
    border-radius: 8px;
  }
  .card--back .product-photo { left: 330px; top: 22px; width: 250px; height: 190px; }
  .card--front .product-photo { left: 380px; top: 30px; width: 220px; height: 150px; }

  .web-url {
    position: absolute; left: 30px; bottom: 26px;
    font-weight: 700; font-size: 30px; letter-spacing: 3px;
    color: var(--brand-purple);
    white-space: nowrap;
  }
  .web-url__prefix { color: var(--brand-blue); }

  .holder {
    position: absolute; left: 30px; top: 132px;
  }
  .holder__name {
    font-family: "Roboto Condensed", "Arial Narrow", sans-serif;
    font-weight: 700; font-size: 24px; color: var(--brand-purple);
  }
  .holder__title {
    font-size: 15px; color: var(--brand-blue); margin-top: 2px;
  }

  .contact-band {
    position: absolute; left: 0; bottom: 0;
    width: 100%; height: 140px;
    background: linear-gradient(180deg, var(--brand-purple) 0%, var(--brand-purple-dark) 100%);
  }
  .contact-band::before {
    content: ""; position: absolute; left: 0; top: 10px;
    width: 100%; height: 3px; background: var(--card-bg);
  }
  .contact-list {
    position: absolute; top: 32px; list-style: none;
  }
  .contact-list--phones { left: 30px; }
  .contact-list--web { left: 260px; }
  .contact-list li {
    display: flex; align-items: center; gap: 10px;
    height: 26px;
    font-size: 15px; letter-spacing: 1px; color: var(--ink-light);
    white-space: nowrap;
  }
  .contact-list svg { width: 16px; height: 16px; flex: none; }
</style>
</head>
<body>
<main class="sheet">

  <section class="card card--back" aria-label="Business card, back">
    <div class="brand">
      <span class="brand__dot"></span>
      <span class="brand__name">Glidewell Depot</span>
    </div>
    <p class="tagline">COMFORT - EXPERIENCE - MOBILITY</p>
    <div class="product-photo" role="img" aria-label="Photo of a folding steel wheelchair with black seat and elevating leg rests"></div>
    <p class="web-url"><span class="web-url__prefix">www.</span>glidewelldepot.com.au</p>
  </section>

  <section class="card card--front" aria-label="Business card, front">
    <div class="brand">
      <span class="brand__dot"></span>
      <span class="brand__name">Glidewell Depot</span>
    </div>
    <div class="holder">
      <p class="holder__name">YOUR NAME</p>
      <p class="holder__title">Your Title</p>
    </div>
    <div class="product-photo" role="img" aria-label="Photo of a folding steel wheelchair with black seat and elevating leg rests"></div>

    <div class="contact-band">
      <ul class="contact-list contact-list--phones">
        <li>
          <svg viewBox="0 0 16 16" aria-hidden="true"><path d="M2 5c0-2 2-3 6-3s6 1 6 3v1h-3V5H5v1H2zM4 7h8l2 6H2z" fill="#f3eef2"/></svg>
          +61 2 5550 2233
        </li>
        <li>
          <svg viewBox="0 0 16 16" aria-hidden="true"><rect x="4" y="1" width="8" height="5" fill="none" stroke="#f3eef2" stroke-width="1.5"/><rect x="1" y="6" width="14" height="7" rx="1" fill="#f3eef2"/><rect x="4" y="11" width="8" height="4" fill="#f3eef2"/></svg>
          +61 2 5550 3355
        </li>
        <li>
          <svg viewBox="0 0 16 16" aria-hidden="true"><rect x="4" y="1" width="8" height="14" rx="1.5" fill="none" stroke="#f3eef2" stroke-width="1.5"/><circle cx="8" cy="12.5" r="1" fill="#f3eef2"/></svg>
          +61 400 555 320
        </li>
      </ul>
      <ul class="contact-list contact-list--web">
        <li>
          <svg viewBox="0 0 16 16" aria-hidden="true"><rect x="1" y="3" width="14" height="10" fill="none" stroke="#f3eef2" stroke-width="1.5"/><path d="M1 3l7 6 7-6" fill="none" stroke="#f3eef2" stroke-width="1.5"/></svg>
          yourname@glidewelldepot.com.au
        </li>
        <li>
          <svg viewBox="0 0 16 16" aria-hidden="true"><circle cx="8" cy="8" r="6.5" fill="none" stroke="#f3eef2" stroke-width="1.5"/><ellipse cx="8" cy="8" rx="3" ry="6.5" fill="none" stroke="#f3eef2" stroke-width="1.2"/><path d="M1.5 8h13" stroke="#f3eef2" stroke-width="1.2"/></svg>
          www.glidewelldepot.com.au
        </li>
        <li>
          <svg viewBox="0 0 16 16" aria-hidden="true"><path d="M8 1a5 5 0 0 0-5 5c0 4 5 9 5 9s5-5 5-9a5 5 0 0 0-5-5z" fill="#f3eef2"/><circle cx="8" cy="6" r="2" fill="#6b2a5c"/></svg>
          Unit 4, 18 Fernleigh Road, Marsden
        </li>
      </ul>
    </div>
  </section>

</main>
</body>
</html>
```